Growing Wellness Company Needs an Amazing Cover for a series of Booklets

We are publishing our own series of booklets on health & wellness topics, called Vital Spark Primers and need an inspiring, modern design for the cover. We are beginning with the Title Diabetes: Type 2, but we will use this design for other titles later one.

SIZE:
This will be the front and back of a 8.5 x 5.5 booklet, plus 2 sample interior pages.

COLOR:
We are an industry leaders and prefer touse vibrant colors and designs to inspire our clients to change to a healthier lifestyle.

REQUIREMENTS:
I am attaching our Vital Spark logo, which needs to be on each cover, but does not need to be the focal point. You may you the words vital spark or just the b logo. The topic/title needs to be no lower than 1/2" from the top of the cover.

I'm attaching some samples of items I like, but please be creative!
If you would like to see some of our other in-house samples of publications send me a message and I'll show you. I will give detailed feedback so dive in and get creative!
Updates

FRONT COVER: 
1. Can you please make sure the title is in the top 1.5" of the page, i can't tell from this view. 
Type 2 Diabetes (1st line, bigger) 
A Simple Guide to Understanding & Controlling Your Blood Sugar (Second Row, much smaller) this can also be below the 1.5" line if it needs to be. 
3.We would like to see three shapes maybe toward the bottom with these words in them, one word per shape. inspire, equip, succeed 

IMAGE 
1. We would like you to leave a placeholder for an image, but would like to see different shapes, such as a rounded square or rectangle or a rectangle with two square corners and two rounded corners. 
2. Please play with some different border options as well,

BACKSIDE 
1. please put our information on the back side on the bottom, small. the information i will put in a file on the brief, the 2nd page has our address, phone, etc. 
2. Add our MC logo (attached as an image in the design brief)

Thanks! looking forward to what else you have. 

Reason: I want to give more time to get more/better designs in, i know this is a little more involved project.

Reason: Still not happy with designs, would like to see more.

Hello - thank you for submitting designs, the designs are getting a little too busy....here is a website I love the simplicity of...thanks!  http://www.brindlevalecare.example   

Reason: We are getting closer to narrowing it down, I want to give the designers a few more days to tweak their designs, then i will ask the final 2 or 3 to submit a couple version of the inside pages. I will supply text for those so you know what you're working with. Thanks!

Target Market(s)

Our clients are adults, about 50/50 men & women in the age range from 20-70 with most being in their early 50's. from high school education up to professional degrees

Industry/Entity Type

Industry

Font styles to use
Serif
Sans Serif
Script

Colors
a64599
e34197
00a98f
9bcb3c
ffc214
f78f20
f37122
0492cd
6a439a

Requirements
Must have
• Eye catching, inspiring design that entices people to read our booklet:

I need a front and back cover and 2 interior page samples , we will be using more of an info graphic style inside possible with a few actual photographs

FRONT COVER REQUIREMENTS:
Title (must be no lower than 1.5" below the top)
Vital Spark Logo (attached in pink and green)
Meadowcrest Wellness' Logo

BACK COVER REQUIREMENTS:
a place for summary text
meadowcrest wellness contact information
a place for an item # (can be small, no barcode)
Nice to have
• the colors i chose are samples, does not need to include every color, each title we write will have a different color story

I can appreciate a white cover with some amazing art of pops of color, but i would also love a really rich color with subtle tone on tone things (see the navy blue cover picture)
Should not have
• boring colors, lots of pictures, typical booklet design

```html
<!DOCTYPE html>
<html lang="en">
<head>
<meta charset="utf-8">
<title>Vital Spark Primers – Type 2 Diabetes cover spread</title>
<link rel="stylesheet" href="https://fonts.googleapis.com/css2?family=Open+Sans:wght@400;600;700;800&display=swap">
<style>
  :root {
    --pink: #e34197;
    --magenta: #a64599;
    --teal: #00a98f;
    --green: #9bcb3c;
    --orange: #f78f20;
    --blue: #0492cd;
    --navy: #1f4f7a;
    --ink: #4a4a4a;
    --paper: #ffffff;
    --stage: #ececec;
  }
  * { box-sizing: border-box; margin: 0; padding: 0; }
  html, body { width: 849px; height: 1200px; overflow: hidden; }
  body {
    background: var(--stage);
    font-family: "Open Sans", Arial, sans-serif;
    color: var(--ink);
    position: relative;
  }
  .spread {
    position: absolute;
    left: 20px; top: 287px;
    width: 809px; height: 625px;
    display: flex;
    box-shadow: 0 6px 24px rgba(0,0,0,.18);
  }
  .page {
    position: relative;
    width: 404.5px; height: 625px;
    background: var(--paper);
    overflow: hidden;
  }
  .page + .page { border-left: 1px solid #e4e4e4; }
  .shapes { position: absolute; inset: 0; width: 100%; height: 100%; }

  /* brand name block */
  .brand {
    position: absolute;
    display: flex; align-items: center; gap: 6px;
    font-weight: 700; font-size: 13px; color: var(--teal);
  }
  .brand-square { width: 14px; height: 14px; background: var(--green); }

  /* front cover */
  .front .brand { top: 22px; right: 22px; }
  .title-block { position: absolute; left: 28px; top: 44px; }
  .title {
    font-size: 38px; font-weight: 800; color: var(--navy); line-height: 1;
    letter-spacing: -0.5px;
  }
  .title .title-light { font-weight: 400; font-size: 24px; color: var(--ink); margin-left: 4px; }
  .subtitle {
    margin-top: 10px;
    background: var(--teal); color: #fff;
    font-size: 10.5px; font-weight: 600;
    padding: 5px 14px 5px 10px;
    border-radius: 0 14px 14px 0;
    display: inline-block;
  }
  .photo {
    position: absolute; left: 150px; top: 130px; width: 254px; height: 330px;
    border-radius: 40px 0 0 40px;
    background: radial-gradient(ellipse at 45% 40%, #f3dccd 0%, #e9c6b2 45%, #dbe4ea 100%);
  }
  .floral-front {
    position: absolute; left: 30px; top: 380px; width: 190px; height: 150px;
    border-radius: 50%;
    background: radial-gradient(ellipse at 50% 50%, #6cc3ec 0%, #b8e1f5 55%, rgba(255,255,255,0) 75%);
  }
  .pillar {
    position: absolute; border-radius: 50%;
    border: 4px solid #fff;
    box-shadow: 0 2px 6px rgba(0,0,0,.2);
    display: flex; align-items: center; justify-content: center;
    color: #fff; font-weight: 600; font-size: 15px;
  }
  .pillar-inspire { background: var(--blue); width: 82px; height: 82px; left: 60px; top: 500px; }
  .pillar-equip { background: var(--orange); width: 74px; height: 74px; left: 160px; top: 488px; }
  .pillar-succeed { background: var(--green); width: 78px; height: 78px; left: 256px; top: 458px; }

  /* back cover */
  .back .brand { top: 8px; left: 18px; background: #fff; padding: 4px 8px; }
  .back-heading {
    position: absolute; left: 0; top: 64px;
    background: var(--teal); color: #fff;
    font-size: 11px; font-weight: 700;
    padding: 6px 18px 6px 22px;
    border-radius: 0 14px 14px 0;
  }
  .partner {
    position: absolute; right: 20px; top: 56px;
    display: flex; align-items: center; gap: 6px;
    font-size: 10px; font-weight: 700; color: var(--teal);
  }
  .partner-circle { width: 22px; height: 22px; border-radius: 50%; background: var(--green); }
  .summary {
    position: absolute; left: 22px; top: 110px; width: 230px;
    font-size: 9.5px; line-height: 1.65; color: var(--ink);
  }
  .floral-back {
    position: absolute; left: 180px; top: 350px; width: 200px; height: 180px;
    border-radius: 50%;
    background: radial-gradient(ellipse at 50% 50%, #6cc3ec 0%, #b8e1f5 55%, rgba(255,255,255,0) 75%);
  }
  .contact {
    position: absolute; left: 22px; top: 440px; width: 150px;
    font-size: 7.5px; line-height: 1.5; color: var(--ink);
  }
  .contact strong { font-weight: 700; }
</style>
</head>
<body>
  <div class="spread">
    <section class="page back">
      <svg class="shapes" viewBox="0 0 404.5 625" preserveAspectRatio="none" aria-hidden="true">
        <path d="M0 0 H404.5 V34 C300 46 200 42 120 40 C80 40 40 46 0 56 Z" fill="var(--pink)"/>
        <path d="M0 0 H150 C110 12 60 30 0 46 Z" fill="var(--green)"/>
        <path d="M0 560 C120 520 260 540 404.5 590 V625 H0 Z" fill="var(--green)"/>
        <path d="M0 585 C140 560 280 580 404.5 610 V625 H0 Z" fill="var(--teal)"/>
      </svg>
      <div class="brand"><span class="brand-square"></span>Vital Spark</div>
      <div class="back-heading">Lorem ipsum dolor sit amet</div>
      <div class="partner"><span class="partner-circle"></span>Meadowcrest Wellness</div>
      <p class="summary">Type 2 diabetes affects millions of adults, yet small daily choices can make a real difference. This guide explains how blood sugar works, what your numbers mean and how food, movement, sleep and stress shape your health. Clear charts and simple steps help you plan meals, track progress and talk with your care team. Inside you will find practical tips, easy checklists and encouraging stories from people who have taken charge of their health. Whether you were just diagnosed or have lived with diabetes for years, this primer will help you feel ready to set goals and reach them, one step at a time.</p>
      <div class="floral-back" role="img" aria-label="Soft blue watercolour floral splash"></div>
      <div class="contact">
        <strong>Meadowcrest Wellness</strong><br>
        48 Orchard Lane, Suite 200<br>
        Fairhaven, OR 97000<br>
        Phone 555-0142<br>
        www.brindlevalecare.example<br>
        Item # VS-0201
      </div>
    </section>

    <section class="page front">
      <div class="photo" role="img" aria-label="Portrait photograph of a smiling woman with clear skin"></div>
      <div class="floral-front" role="img" aria-label="Soft blue watercolour floral splash"></div>
      <svg class="shapes" viewBox="0 0 404.5 625" preserveAspectRatio="none" aria-hidden="true">
        <path d="M0 160 C60 260 70 420 30 625 H0 Z" fill="var(--pink)"/>
        <path d="M404.5 300 C360 420 330 520 300 625 H404.5 Z" fill="var(--magenta)"/>
        <path d="M0 560 C140 560 280 500 404.5 400 V470 C300 560 160 610 60 625 H0 Z" fill="var(--green)"/>
        <path d="M0 600 C140 600 280 560 404.5 470 V520 C320 590 200 625 120 625 H0 Z" fill="var(--teal)"/>
      </svg>
      <div class="brand"><span class="brand-square"></span>Vital Spark</div>
      <div class="title-block">
        <h1 class="title">Type 2<span class="title-light">Diabetes</span></h1>
        <p class="subtitle">A Simple Guide to Understanding &amp; Controlling Your Blood Sugar</p>
      </div>
      <div class="pillar pillar-inspire">inspire</div>
      <div class="pillar pillar-equip">equip</div>
      <div class="pillar pillar-succeed">succeed</div>
    </section>
  </div>
</body>
</html>
```